Energy Company needs a Business Card Design

We need a business card design for a new company based in Singapore called Tarn Energy. Tarn Energy is a producer of renewable energies largely for the biofuels market. Sourced entirely from sustainable resources, Tarn Energy aims to be a fully integrated oil company operating in 100% sustainable way. We would like to see designs that use the same colours as the attached file.

Industry/Entity Type

Business

```html
<!DOCTYPE html>
<html lang="en">
<head>
<meta charset="utf-8">
<title>Tarn Energy – Business Card</title>
<link href="https://fonts.googleapis.com/css2?family=Montserrat:wght@400;500;600;700&display=swap" rel="stylesheet">
<style>
  :root {
    --backdrop: #dcdcda;
    --card-white: #ffffff;
    --card-black: #0a0a0a;
    --leaf-green: #8cc63f;
    --silver: #c9ccce;
    --silver-dark: #9a9ea1;
    --logo-grey: #8a8e91;
    --rule: #3a3a3a;
    --text-light: #ffffff;
  }
  * { margin: 0; padding: 0; box-sizing: border-box; }
  html, body { width: 1200px; height: 900px; overflow: hidden; }
  body {
    background: var(--backdrop);
    font-family: "Montserrat", sans-serif;
    position: relative;
  }
  .card {
    position: absolute;
    left: 290px;
    width: 620px;
    height: 355px;
    border-radius: 18px;
    overflow: hidden;
    box-shadow: 0 6px 18px rgba(0,0,0,0.18);
  }
  .card-front { top: 60px; background: var(--card-white); }
  .card-back { top: 470px; background: var(--card-black); }

  .wordmark {
    display: flex;
    align-items: center;
    gap: 12px;
    font-weight: 600;
    letter-spacing: 1px;
  }
  .wordmark .dot {
    width: 16px; height: 16px; border-radius: 50%;
    background: var(--leaf-green);
  }
  .card-front .wordmark {
    position: absolute;
    top: 50%; left: 50%;
    transform: translate(-50%, -50%);
    font-size: 52px;
    color: var(--logo-grey);
  }
  .card-back .wordmark {
    position: absolute;
    top: 48px; left: 40px;
    font-size: 40px;
    color: var(--silver);
  }

  .holder {
    position: absolute;
    right: 40px; top: 92px;
    text-align: right;
  }
  .holder-name {
    color: var(--leaf-green);
    font-weight: 700;
    font-size: 21px;
    letter-spacing: 1px;
  }
  .holder-title {
    color: var(--text-light);
    font-size: 13px;
    font-weight: 500;
    letter-spacing: 1px;
    margin-top: 2px;
  }
  .divider {
    position: absolute;
    left: 40px; right: 40px; top: 160px;
    height: 1px;
    background: var(--rule);
  }
  .contacts {
    position: absolute;
    top: 188px; left: 40px; right: 40px;
    display: flex;
    gap: 40px;
  }
  .contact-group { display: flex; flex-direction: column; gap: 10px; }
  .contact-line {
    display: flex; align-items: center; gap: 10px;
    color: var(--text-light);
    font-size: 16px;
    font-weight: 500;
    letter-spacing: 1px;
  }
  .contact-line svg { width: 14px; height: 14px; flex: none; }

  .footer-bands { position: absolute; left: 0; bottom: 0; width: 620px; height: 100px; }
  .address {
    position: absolute;
    left: 24px; bottom: 18px;
    display: flex; align-items: center; gap: 10px;
    color: var(--text-light);
    font-size: 17px;
    font-weight: 500;
    letter-spacing: 1.5px;
  }
  .address svg { width: 14px; height: 18px; }
  .tab-label {
    position: absolute;
    right: 36px; bottom: 34px;
    color: #eef0f1;
    font-size: 28px;
    font-weight: 400;
    letter-spacing: 3px;
  }
</style>
</head>
<body>

  <section class="card card-front">
    <div class="wordmark"><span class="dot"></span>Tarn Energy</div>
  </section>

  <section class="card card-back">
    <div class="wordmark"><span class="dot"></span>Tarn Energy</div>

    <div class="holder">
      <div class="holder-name">MARCUS HALE</div>
      <div class="holder-title">President</div>
    </div>

    <div class="divider"></div>

    <div class="contacts">
      <div class="contact-group">
        <div class="contact-line">
          <svg viewBox="0 0 14 14"><rect x="3" y="1" width="8" height="12" rx="1.5" fill="none" stroke="#8cc63f" stroke-width="1.6"/><line x1="5" y1="10.5" x2="9" y2="10.5" stroke="#8cc63f" stroke-width="1.4"/></svg>
          +65 6123 4567
        </div>
        <div class="contact-line">
          <svg viewBox="0 0 14 14"><path d="M3 1.5 L5.5 1.5 L6.5 4.5 L5 5.8 Q6.3 8.4 8.2 9 L9.5 7.5 L12.5 8.5 L12.5 11 Q12.5 12.5 11 12.5 Q2 12 1.5 3 Q1.5 1.5 3 1.5 Z" fill="#8cc63f"/></svg>
          +65 6123 4568
        </div>
      </div>
      <div class="contact-group">
        <div class="contact-line">
          <svg viewBox="0 0 14 14"><rect x="1" y="3" width="12" height="8" fill="none" stroke="#8cc63f" stroke-width="1.4"/><path d="M1 3 L7 8 L13 3" fill="none" stroke="#8cc63f" stroke-width="1.4"/></svg>
          info@tarnenergy.com
        </div>
        <div class="contact-line">
          <svg viewBox="0 0 14 14"><circle cx="7" cy="7" r="5.6" fill="none" stroke="#8cc63f" stroke-width="1.3"/><ellipse cx="7" cy="7" rx="2.4" ry="5.6" fill="none" stroke="#8cc63f" stroke-width="1.1"/><line x1="1.4" y1="7" x2="12.6" y2="7" stroke="#8cc63f" stroke-width="1.1"/></svg>
          www.tarnenergy.com
        </div>
      </div>
    </div>

    <svg class="footer-bands" viewBox="0 0 620 100" aria-hidden="true">
      <defs>
        <linearGradient id="silver-band" x1="0" y1="0" x2="0" y2="1">
          <stop offset="0" stop-color="#e4e6e7"/>
          <stop offset="1" stop-color="#9a9ea1"/>
        </linearGradient>
      </defs>
      <path d="M380 100 L380 60 Q380 30 410 30 L620 30 L620 100 Z" fill="url(#silver-band)"/>
      <path d="M0 55 L380 55 Q395 55 400 45 L410 33 L410 100 L0 100 Z" fill="var(--leaf-green)"/>
    </svg>

    <div class="address">
      <svg viewBox="0 0 14 18"><path d="M7 1 Q13 1 13 7 Q13 11 7 17 Q1 11 1 7 Q1 1 7 1 Z" fill="#fff"/><circle cx="7" cy="7" r="2.3" fill="#8cc63f"/></svg>
      48 Keppel Road, Singapore 089057
    </div>
    <div class="tab-label">ENERGY</div>
  </section>

</body>
</html>
```